Harborline Quoting
Business Cards and Stationery for Service Co
Simple
Dane Corwell
Vice President
20436 SW 47th Avenue Suite 3105 Vancouver, WA 97531
danec@harborlinequoting.com
www.harborlinequoting.com
Please keep it simple and professional.
Just the logo

```html
<!DOCTYPE html>
<html lang="en">
<head>
<meta charset="utf-8">
<title>Harborline Quoting Stationery</title>
<link href="https://fonts.googleapis.com/css2?family=Open+Sans:wght@400;700&family=Great+Vibes&display=swap" rel="stylesheet">
<style>
:root{
  --orange:#e8622c;
  --orange-dark:#c9501f;
  --paper:#ffffff;
  --ink:#4d4d4d;
  --muted:#9a9a9a;
  --board:#d9d9d9;
  --topbar:#3a3a3a;
}
*{box-sizing:border-box;margin:0;padding:0}
html,body{width:1200px;height:247px;overflow:hidden}
body{background:var(--board);font-family:"Open Sans",sans-serif;color:var(--ink);position:relative}
.topbar{position:absolute;left:0;top:0;width:1200px;height:14px;background:var(--topbar)}
.item{position:absolute;background:var(--paper);box-shadow:0 1px 3px rgba(0,0,0,.25);overflow:hidden}
.item.orange{background:var(--orange);color:#fff}
.brand{display:flex;align-items:center;gap:3px;font-weight:700;color:var(--orange);white-space:nowrap}
.brand .mark{width:1em;height:1em;background:var(--orange)}
.orange .brand{color:#fff}
.orange .brand .mark{background:#fff}
.tiny{font-size:3px;line-height:1.4;white-space:nowrap}
.line{height:2px;background:#e1e1e1;margin-top:3px}
.band{position:absolute;left:0;right:0;bottom:0;height:6px;background:var(--orange)}
.script{font-family:"Great Vibes",cursive;color:var(--ink)}
.faint-circle{position:absolute;border-radius:50%;background:rgba(232,98,44,.08)}
</style>
</head>
<body>
<div class="topbar"></div>

<!-- business cards -->
<div class="item card" style="left:12px;top:86px;width:118px;height:62px;padding:18px 12px">
  <div class="brand" style="font-size:9px"><span class="mark"></span>Harborline Quoting</div>
</div>
<div class="item card orange" style="left:12px;top:152px;width:118px;height:30px;padding:6px 8px">
  <div class="tiny" style="font-size:5px;font-weight:700">Dane Corwell</div>
  <div class="tiny">Vice President</div>
  <div class="tiny">danec@harborlinequoting.com</div>
</div>
<div class="item card" style="left:12px;top:190px;width:60px;height:40px;padding:5px">
  <div class="brand" style="font-size:4px"><span class="mark"></span>Harborline Quoting</div>
</div>
<div class="item card orange" style="left:78px;top:190px;width:60px;height:40px;padding:5px">
  <div class="tiny">www.harborlinequoting.com</div>
</div>
<div class="item card" style="left:140px;top:150px;width:70px;height:42px;background:#8a8a8a">
  <div class="band" style="height:42px;width:18px;left:auto"></div>
</div>

<!-- letterhead one -->
<div class="item letterhead" style="left:264px;top:20px;width:130px;height:218px;padding:10px">
  <div class="brand" style="font-size:7px"><span class="mark"></span>Harborline Quoting</div>
  <div style="margin-top:20px" class="tiny">Dear client, thank you for your request.</div>
  <div class="line"></div><div class="line"></div><div class="line"></div><div class="line"></div>
  <div class="line"></div><div class="line" style="width:60%"></div>
  <div style="position:absolute;bottom:10px;left:10px" class="tiny">20436 SW 47th Avenue Suite 3105 Vancouver, WA 97531</div>
  <div class="band" style="height:4px"></div>
</div>

<!-- orange sheet -->
<div class="item orange" style="left:408px;top:20px;width:74px;height:120px;padding:8px">
  <div class="brand" style="font-size:5px"><span class="mark"></span>Harborline Quoting</div>
</div>

<!-- envelopes -->
<div class="item envelope" style="left:400px;top:150px;width:120px;height:48px;padding:6px">
  <div class="brand" style="font-size:5px"><span class="mark"></span>Harborline Quoting</div>
  <div class="band" style="height:4px"></div>
</div>
<div class="item envelope orange" style="left:410px;top:204px;width:110px;height:34px">
  <svg width="110" height="34" viewBox="0 0 110 34"><path d="M0 0 L55 20 L110 0" fill="none" stroke="var(--orange-dark)" stroke-width="1"/></svg>
</div>

<!-- compliment slip -->
<div class="item slip" style="left:530px;top:150px;width:150px;height:88px;padding:8px">
  <div class="brand" style="font-size:6px"><span class="mark"></span>Harborline Quoting</div>
  <div class="script" style="font-size:15px;margin-top:22px;text-align:center">With Compliments</div>
  <div class="band" style="height:4px"></div>
</div>

<!-- orange letterhead -->
<div class="item orange" style="left:540px;top:20px;width:140px;height:120px;padding:10px">
  <div class="brand" style="font-size:7px"><span class="mark"></span>Harborline Quoting</div>
  <div class="tiny" style="position:absolute;bottom:8px;left:10px">www.harborlinequoting.com</div>
</div>

<!-- small cards -->
<div class="item" style="left:692px;top:20px;width:90px;height:52px;padding:8px">
  <div class="brand" style="font-size:5px"><span class="mark"></span>Harborline Quoting</div>
  <div class="tiny" style="margin-top:8px">Dane Corwell · Vice President</div>
</div>
<div class="item" style="left:692px;top:78px;width:90px;height:52px;padding:8px">
  <div class="tiny">Short note card for quick messages.</div>
  <div class="line"></div><div class="line"></div>
  <div class="band" style="height:3px"></div>
</div>

<!-- letterhead two -->
<div class="item letterhead" style="left:795px;top:20px;width:165px;height:218px;padding:12px">
  <div class="faint-circle" style="width:110px;height:110px;left:28px;top:60px"></div>
  <div class="brand" style="font-size:8px"><span class="mark"></span>Harborline Quoting</div>
  <div class="tiny" style="margin-top:24px">Project estimate summary attached for review.</div>
  <div class="line"></div><div class="line"></div><div class="line"></div>
  <div class="line"></div><div class="line" style="width:55%"></div>
  <div style="position:absolute;bottom:10px;left:12px" class="tiny">danec@harborlinequoting.com · www.harborlinequoting.com</div>
  <div class="band" style="height:4px"></div>
</div>

<!-- folder -->
<div class="item orange folder" style="left:980px;top:16px;width:210px;height:222px;padding:16px">
  <div class="brand" style="font-size:11px"><span class="mark"></span>Harborline Quoting</div>
  <div style="position:absolute;left:0;right:0;bottom:0;height:80px;background:var(--orange-dark)"></div>
  <div class="tiny" style="position:absolute;bottom:10px;left:16px;font-size:4px">20436 SW 47th Avenue Suite 3105 Vancouver, WA 97531</div>
</div>
</body>
</html>
```